Silver Heron Staffing Agency

I need to make a brochure/catalogue that represent our company, telling our clients what we do, our values, fields of industry that we taken care of, so they know who we are, what we did, and how we do it.
I do have a logo and simple brochure design before that i really need to upgrade (i will give it as an example on this attachment).

What I want in the new design is :
1. More pictures and little bit of explanation in each industry we work with.
2. Attractive design that make people LOOK at the brochure and not just throw it in the trash.
3. Still use the combination color of the company logo itself, which is Golden Brown.

```html
<!DOCTYPE html>
<html lang="en">
<head>
<meta charset="utf-8">
<title>Silver Heron Staffing Agency – Tri-fold Brochure</title>
<link href="https://fonts.googleapis.com/css2?family=Open+Sans:ital,wght@0,400;0,600;0,700;0,800;1,600&family=Montserrat:wght@800&family=Oswald:wght@600&display=swap" rel="stylesheet">
<style>
:root{
  --gold:#a8862f;
  --gold-light:#c9a544;
  --black:#000;
  --ink:#2b2b2b;
  --paper:#f1f1f1;
  --white:#fff;
  --bg:#6d6d6d;
}
*{margin:0;padding:0;box-sizing:border-box}
html,body{width:814px;height:1200px;overflow:hidden}
body{background:var(--bg);font-family:"Open Sans",Arial,sans-serif;position:relative}
.sheet{position:absolute;left:48px;width:717px;height:508px;display:flex;box-shadow:0 4px 14px rgba(0,0,0,.45)}
.sheet--outside{top:59px}
.sheet--inside{top:623px}
.panel{position:relative;width:239px;height:100%;overflow:hidden}
.panel--black{background:var(--black);color:var(--white)}
.panel--gold{background:var(--gold);color:var(--white)}
.panel--light{background:linear-gradient(135deg,#fafafa,#e9e9e9);color:var(--ink)}
.abs{position:absolute}
.heading{font-size:14px;font-weight:400;letter-spacing:.2px;line-height:1}
.heading b{font-weight:700}
.heading--gold b{color:var(--gold)}
.rule{position:absolute;height:1px}
.body-text{font-size:7.4px;line-height:10.5px;text-align:justify}
.photo{position:absolute}
.photo-frame{position:absolute;inset:5px;border:1px solid var(--gold-light)}

/* outside */
.locations{left:22px;top:58px;display:grid;grid-template-columns:95px 95px;row-gap:4px;font-size:9.6px;line-height:12px}
.photo-strip{position:absolute;left:239px;top:124px;width:478px;height:222px;background:linear-gradient(90deg,#e9e2d8,#f5f2ee 30%,#e6dfd6 60%,#f3f0ec);z-index:2}
.contact{position:absolute;left:0;top:346px;width:239px;text-align:center}
.pill-dark{margin:15px auto 0;width:152px;height:22px;border-radius:11px;background:var(--black);font-size:15px;line-height:22px}
.pill-dark b{font-weight:700}
.contact-line{font-size:8.6px;line-height:12px}
.phone{font-size:13px;font-weight:700;margin-top:6px}
.brand{position:absolute;left:0;top:64px;width:239px;text-align:center;color:var(--gold);font-size:13px;font-weight:700;letter-spacing:1px}
.brand-mark{display:inline-block;width:10px;height:10px;background:var(--gold);margin-right:6px;vertical-align:0}
.slogan{position:absolute;left:0;top:364px;width:239px;text-align:center;font-family:Montserrat,Arial,sans-serif;font-weight:800;font-size:27px;line-height:29px}
.slogan .band{display:inline-block;width:180px;background:linear-gradient(90deg,#a8862f,#d4b35a,#a8862f);color:var(--black)}
.url-pill{position:absolute;left:23px;top:470px;width:194px;height:22px;border:1px solid var(--gold);border-radius:11px;text-align:center;font-size:10.4px;line-height:20px}

/* inside */
.tag{position:absolute;left:20px;height:12px;padding:0 14px 0 8px;font-size:8.6px;font-weight:700;line-height:12px;clip-path:polygon(0 0,100% 0,calc(100% - 8px) 100%,0 100%)}
.tag--gold{background:var(--gold);color:var(--white)}
.tag--dark{background:#2a2a2a;color:var(--white)}
.small{position:absolute;left:20px;width:202px;font-size:5.9px;line-height:8.2px;text-align:justify}
.small--right{left:18px;width:202px}
.sub{font-weight:700;color:var(--gold);font-size:6.8px}
.industries{position:absolute;left:18px;top:368px;list-style:none;font-weight:700;font-size:11.4px;line-height:18px}
.connect{position:absolute;left:18px;top:422px;width:203px;height:70px;background:var(--gold);text-align:center}
.connect-top{color:var(--white);font-family:Montserrat,Arial,sans-serif;font-weight:800;font-size:16.5px;line-height:17px;padding-top:6px;letter-spacing:1px}
.connect-bottom{position:absolute;left:0;bottom:0;width:100%;height:25px;background:#222;color:var(--white);font-family:Oswald,Arial,sans-serif;font-weight:600;font-size:15px;line-height:25px}
</style>
</head>
<body>

<!-- OUTSIDE -->
<section class="sheet sheet--outside">
  <div class="panel panel--black">
    <h2 class="heading heading--gold abs" style="left:25px;top:23px">YOUR <b>EXCLUSIVE AGENT</b></h2>
    <div class="rule" style="left:25px;top:46px;width:183px;background:var(--gold)"></div>
    <p class="body-text abs" style="left:25px;top:59px;width:181px">Lorem ipsum dolor sit amet, consectetur adipiscing elit, sed do eiusmod tempor incididunt ut labore et dolore magna aliqua. Ut enim ad minim veniam, quis nostrud exercitation ullamco laboris nisi ut aliquip ex ea commodo consequat. Duis aute irure dolor in reprehenderit in voluptate velit esse cillum dolore eu fugiat nulla pariatur. Excepteur sint occaecat cupidatat non proident, sunt in culpa qui officia deserunt mollit anim id est laborum.</p>
    <p class="body-text abs" style="left:25px;top:166px;width:181px">Sed ut perspiciatis unde omnis iste natus error sit voluptatem accusantium doloremque laudantium, totam rem aperiam, eaque ipsa quae ab illo inventore veritatis et quasi architecto beatae vitae dicta sunt explicabo.</p>
    <div class="photo" role="img" aria-label="Casino dealer in a vest smiling at a gaming table" style="left:24px;top:241px;width:192px;height:115px;background:linear-gradient(135deg,#d9d4cf,#8a6a5a 60%,#5a2a28)"><div class="photo-frame"></div></div>
    <div class="photo" role="img" aria-label="Warehouse worker in hard hat and safety vest holding a clipboard" style="left:24px;top:374px;width:192px;height:116px;background:linear-gradient(135deg,#b9b4ad,#8a7d6c 50%,#c9c24a)"><div class="photo-frame"></div></div>
  </div>

  <div class="panel panel--gold" style="overflow:visible">
    <h2 class="heading abs" style="left:21px;top:23px">OUR <b>LOCATIONS</b></h2>
    <div class="rule" style="left:21px;top:46px;width:196px;background:#e8d7a8"></div>
    <ul class="locations abs" style="list-style:none">
      <li>✓ NEW YORK</li><li>✓ DELAWARE</li>
      <li>✓ PENNSYLVANIA</li><li>✓ VIRGINIA</li>
      <li>✓ NEW JERSEY</li><li>✓ GEORGIA</li>
    </ul>
    <div class="photo-strip" role="img" aria-label="Row of smiling hospitality staff in white shirts, chef whites and bow ties"></div>
    <div class="contact">
      <div class="pill-dark">CONTACT <b>INFO</b></div>
      <svg width="8" height="10" viewBox="0 0 8 10" style="margin-top:7px" aria-hidden="true"><circle cx="4" cy="3.5" r="2.6" fill="none" stroke="#111" stroke-width="1"/><path d="M4 6.1V9.5M2 9.5h4" stroke="#111" stroke-width="1"/></svg>
      <p class="contact-line">42 Birch Lane, suite 300<br>Cedar Grove. NJ 07009</p>
      <p class="phone"><svg width="11" height="11" viewBox="0 0 12 12" style="vertical-align:-1px" aria-hidden="true"><circle cx="6" cy="6" r="5.3" fill="none" stroke="#111" stroke-width="1"/><path d="M4 3.3l1.2 1.4-.7.8c.5 1 1.1 1.6 2 2l.8-.7 1.4 1.2-.8.9C5.6 8.7 3.5 6.6 3.3 4.2z" fill="#111"/></svg> 555-201-4830</p>
      <p class="contact-line" style="margin-top:5px">✉ info@silverheronstaffing.com</p>
      <p class="contact-line" style="margin-top:7px">⊕ SilverHeronStaffing.com</p>
    </div>
  </div>

  <div class="panel panel--black">
    <div class="brand"><span class="brand-mark"></span>SILVER HERON Inc.</div>
    <div class="rule" style="left:30px;top:346px;width:180px;height:2px;background:var(--gold)"></div>
    <div class="slogan">YOUR<br>BEST WAY TO<br><span class="band">SUCCEED</span></div>
    <div class="url-pill">SilverHeronStaffing.com</div>
  </div>
</section>

<!-- INSIDE -->
<section class="sheet sheet--inside">
  <div class="panel panel--light">
    <h2 class="heading heading--gold abs" style="left:20px;top:17px">ABOUT <b>US</b></h2>
    <div class="rule" style="left:20px;top:37px;width:196px;background:var(--gold)"></div>

    <div class="tag tag--gold" style="top:54px">History</div>
    <p class="small" style="top:67px">With more than 18 years of experience Silver Heron Staffing provided staffing services to a wide array of locations, all throughout Pennsylvania. Through the last few years we have expanded to 5 other states including New York, New Jersey, Delaware, Virginia and Georgia. Our ethics are a critical building block of our business. Our own success is based on adherence to the highest ethical standards; long-term client relationships, the ability to identify top candidates, and the high-quality professional development of Silver Heron Staffing professionals protecting the confidentiality and interests of clients and candidates.</p>

    <div class="tag tag--gold" style="top:151px">Culture</div>
    <p class="small" style="top:164px">Silver Heron believes in equal opportunity for all, regardless of gender, race, ethic, origin, religion, or handicap. The staffing policies and practices of Silver Heron for our organization, our clients and candidates are fully non-discriminatory. Our employees are our most valuable asset. We strive to create a work environment of professionalism, trust and respect that will continuously provide our staff with motivation, challenge, and professional growth to aim our most important goal; CLIENT SATISFACTION.</p>

    <div class="tag tag--gold" style="top:232px">Mission</div>
    <p class="small" style="top:245px">Silver Heron is more than a staffing company; we want to become your business partner. We understand that payroll and employee-service overhead can be one of the largest expenses for your business. Through our partnership-network programs Silver Heron can help you reduce the hard-costs of your business expenses. We take responsibility for all our placed employees, including payroll taxes and benefits.</p>

    <div class="tag tag--gold" style="top:304px">Our Process</div>
    <p class="small" style="top:317px">Our screening process includes a thorough interview with each potential candidate to give us insight into the candidate's previous work history, skills, communication abilities and career goals as well as reference checks with their previous employers.</p>

    <div class="tag tag--gold" style="top:361px">Staffing Solutions</div>
    <p class="small" style="top:374px">Silver Heron's personalized services, expertise and afford-able rates are key factors of our success and being our client's choice staffing agency. Our contingent and contract-to-hire employees are looking for flexible careers in New York, New Jersey, Pennsylvania, Delaware, Virginia and Georgia.</p>

    <div class="photo" role="img" aria-label="Group of workers from many trades: chef, builder, doctor, cleaner and a smiling man with a thumbs up" style="left:0;top:427px;width:239px;height:81px;background:linear-gradient(180deg,rgba(240,240,240,0),#b7a58e 45%,#6c6560)"></div>
  </div>

  <div class="panel panel--gold">
    <h2 class="heading abs" style="left:18px;top:17px">WHY <b>STAFFING?</b></h2>
    <div class="rule" style="left:18px;top:37px;width:196px;background:#e8d7a8"></div>

    <div class="tag tag--dark" style="top:54px;left:18px">Avoid Unemployment Claims</div>
    <p class="small small--right" style="top:67px">The temporary staff personnel is an employee of the staffing agency and not the business, there is no concern about the per-son filing for unemployment when their services are no longer needed by the business reducing overall operating and human resources costs.</p>

    <div class="tag tag--dark" style="top:114px;left:18px">Improve Productivity</div>
    <p class="small small--right" style="top:127px">By bringing in temporary staff to handle the extra work-load, your full-time employees can continue to focus on their main job tasks while maintaining their productivity.</p>

    <div class="tag tag--dark" style="top:165px;left:18px">Increasing Flexibility</div>
    <p class="small small--right" style="top:178px">Temporary employees can be brought in to cover the vacation of an employee or maternity leave or a seasonal work. Whether it is a few hours a week or on a full-time basis, using a staffing agency can avoid the permanent commitment that a full-time employee requires.</p>

    <div class="tag tag--dark" style="top:224px;left:18px">Decrease Cost</div>
    <p class="small small--right" style="top:237px">Employing temporary staff can decrease overhead costs such as overtime for regular, full-time employees as well as additional benefits that the business does not have to provide to a temporary staff member.</p>

    <div class="tag tag--dark" style="top:276px;left:18px">Contract To Hire</div>
    <p class="small small--right" style="top:289px">Reduce the risk of making a bad hire by evaluating a candidate's performance in your work environment. You can choose to add workers to your permanent team or requesting another worker for your evaluation.</p>

    <h2 class="heading abs" style="left:18px;top:341px">INDUSTRIES <b>WE SERVE</b></h2>
    <div class="rule" style="left:18px;top:355px;width:196px;background:#e8d7a8"></div>
    <ul class="industries">
      <li>» WAREHOUSING</li><li>» HOTEL</li><li>» CASINO</li><li>» PAPER MAILLING</li><li>» TRANSPORTATION</li><li>» LANDFILL</li><li>» FOOD HANDLING</li>
    </ul>
    <div class="photo" role="img" aria-label="Smiling businessman in shirt and tie holding a clipboard" style="left:134px;top:368px;width:105px;height:140px;background:linear-gradient(180deg,rgba(168,134,47,0),#c9d3e6 40%,#8fa0c0)"></div>
  </div>

  <div class="panel panel--light">
    <h2 class="heading heading--gold abs" style="left:18px;top:17px">WHY CHOOSE <b>OUR SERVICES?</b></h2>
    <p class="small small--right" style="top:52px;font-size:7px;line-height:9.4px">Our commitment is to deliver the highest possible level of service, professionalism and integrity. Our focus is on delivering results and building long term client relationships by providing top quality candidates.</p>
    <p class="small small--right" style="top:93px"><span class="sub">Employee Benefits:</span><br>Workers are paid on a timely weekly basis. Our system responds to worker's need for payment immediately.</p>
    <p class="small small--right" style="top:123px"><span class="sub">Workers' Compensation:</span><br>We provide workers' compensation for our employees while on assignment. If an injury occurs, we handle all claims and expenses. Our safety and risk depart-ment will help reduce injuries and will ensure high rates of safety compliance.</p>

    <div class="tag tag--dark" style="top:170px;left:18px">Availability and Flexibility</div>
    <p class="small small--right" style="top:183px">Our temporary staff has proven to be available and ready for work in a timely and efficient manner. Our services will be crafted to your needs and specifications ensuring that you are not forced into any unnecessary liabilities.</p>

    <div class="tag tag--dark" style="top:224px;left:18px">Availability and Flexibility</div>
    <p class="small small--right" style="top:237px">Our temporary staff has proven to be available and ready for work in a timely and efficient manner. Our services will be crafted to your needs and specifications ensuring that you are not forced into any unnecessary liabilities.</p>

    <div class="tag tag--dark" style="top:277px;left:18px">We Save you both TIME and MONEY</div>
    <p class="small small--right" style="top:290px">Competitive rates to keep your business on budget. We bill only for employee's hours approved by you.</p>
    <p class="small small--right" style="top:315px">Our business was built on a strong reputation for providing quality service. Part of that reputation stems from an unmatched focus on developing a deep understanding of the job market. We do our best to keep up to date on industry trends, job market patterns, and hiring practices. We believe that knowledge is a driving factor in staffing agency success, and we work with our clients and candidates so they are in the best position possible to accomplish their employment goals.</p>
    <p class="small small--right" style="top:378px;font-style:italic;font-weight:600">When you are looking for a qualified candidate or when you need a new job, trust the experts at Silver Heron Staffing Services. Let us put our world-class cus-tomer service and staffing expertise to work for you!</p>

    <div class="connect">
      <div class="connect-top">CONNECTING<br>OPPORTUNITY</div>
      <div class="connect-bottom">WITH TODAY'S TOP TALENT</div>
    </div>
  </div>
</section>

</body>
</html>
```